Publisher needs a book cover design for ‘The Lantern Keeper's Winter Ledger’ book

We need a book cover (front, back, spine) for the 2nd edition of a book entitled ‘The Lantern Keeper's Winter Ledger’ and subtitled ‘a neglected chapter of harbour trade, river tolls and market charter reform’ (inverted commas not to be part of the title and subtitle). The author is Malcolm Pettigrew. The publisher is Halvenmoor Press. The finished size of the paperback version will be the industry standard 9" x 6". There will be paperback, hardback, and e-book versions. The final number of pages is expected to be in the region 150-180 pages. Text for the back cover is not yet available, but at the bottom of the back cover should be publisher logo (rectangular) on the left and space for the ISBN bar code on the right. The circular logo should be on the spine. The design should be original and not include any stock images that have been created by someone else or may require obtaining a copyright licence to use. Symbols in common use and not copyrighted are probably ok. There are no required images, photographs or symbols except the publisher logo at the left bottom of the back cover and lower spine. Spine lettering should be UK/US style with the top of the writing nearest the front cover. The designer is free to be creative using appropriate diagrams, symbols or abstract designs. Rectangular and circular variants of the publisher logo are attached. Designers are assured that when evaluating designs absolutely no notice whatsoever is taken of a designer's Sketch Bazaar ranking or status; We are completely output driven, so what matters is the design, not the ranking or status of the designer. In a similar way, designs are not evaluated as 'good' or 'bad' - the winning design will be chosen after review by a design review panel and is not decided arbitrarily by a single person. All submitted designs should be capable of effective copyright assignment.

Target Market(s)

Practitioners, parents, teachers, pupils and academics concerned with child protection, safeguarding and the elimination of emotional abuse of children in the classroom

Font styles to use
Serif
Sans Serif

Requirements
Must have
• • Title, author, edition, subtitle, publisher logo
Nice to have
• • Originality, innovation
Should not have
• • Stock images or anything else requiring additional copyright discussions and negotiations.

```html
<!DOCTYPE html>
<html lang="en">
<head>
<meta charset="utf-8">
<title>The Lantern Keeper's Winter Ledger – Cover Spread</title>
<link href="https://fonts.googleapis.com/css2?family=Libre+Bodoni:wght@400;700&family=Libre+Baskerville:wght@700&family=Source+Serif+4:wght@400&display=swap" rel="stylesheet">
<style>
  :root {
    --paper: #ffffff;
    --crop: #555555;
    --navy: #0a1488;
    --violet: #6464bc;
    --slate: #3a5a62;
    --moss: #5e8a3e;
    --lime: #b4ff08;
    --title-green: #1a7a0a;
    --spine-lime: #c8ff4a;
    --edition-rule: #a6e81a;
    --body-ink: #1e1e24;
    --subtitle-ink: #3a463a;
  }
  * { margin: 0; padding: 0; box-sizing: border-box; }
  html, body { width: 1200px; height: 1028px; overflow: hidden; background: var(--paper); }
  .canvas { position: relative; width: 1200px; height: 1028px; }

  .crop-marks { position: absolute; inset: 0; }

  .cover {
    position: absolute; left: 35px; top: 101px; width: 1132px; height: 823px; overflow: hidden;
    background:
      radial-gradient(ellipse 210px 230px at 30px 440px, rgba(255,255,255,1) 0%, rgba(255,255,255,.85) 45%, rgba(255,255,255,0) 100%),
      linear-gradient(145deg, var(--violet) 0%, #2a2aa8 22%, var(--navy) 34%, #24386e 44%, var(--slate) 52%, var(--moss) 62%, #98d820 76%, var(--lime) 88%, var(--lime) 100%);
  }
  .cover::after {
    content: ""; position: absolute; inset: 0;
    background: linear-gradient(to top right, rgba(140,160,160,.9) 0%, rgba(140,160,160,0) 35%);
    pointer-events: none;
  }

  /* Back cover */
  .back-panel {
    position: absolute; left: 81px; top: 93px; width: 406px; height: 648px; border-radius: 17px; z-index: 1;
    background: linear-gradient(165deg, rgba(255,255,255,.6) 0%, rgba(255,255,255,.4) 40%, rgba(255,255,255,.7) 100%);
  }
  .blurb {
    position: absolute; left: 20px; top: 21px; width: 184px;
    font-family: "Source Serif 4", serif; font-size: 16px; line-height: 21.4px; color: var(--body-ink);
  }
  .blurb p + p { margin-top: 10px; }
  .column-rule { position: absolute; left: 223px; top: 58px; width: 1px; height: 450px; background: rgba(255,255,255,.85); }
  .author-photo { position: absolute; left: 245px; top: 113px; width: 48px; height: 59px;
    background: linear-gradient(160deg, #6b4a32, #a0704e 50%, #3a2a22); }
  .about {
    position: absolute; left: 241px; top: 180px; width: 150px;
    font-family: "Source Serif 4", serif; color: var(--body-ink);
  }
  .about h2 { font-weight: 400; font-size: 13.4px; margin-bottom: 10px; }
  .about p { font-size: 13.2px; line-height: 17.1px; }
  .about p + p { margin-top: 8px; }
  .publisher-mark {
    position: absolute; left: 22px; top: 574px; display: flex; align-items: center; gap: 6px;
    font-family: "Source Serif 4", serif; font-size: 15px; letter-spacing: .03em; color: #111; white-space: nowrap;
  }
  .publisher-mark .dot { width: 34px; height: 34px; border-radius: 50%; background: #111; flex: none; }
  .isbn-space { position: absolute; left: 230px; top: 541px; width: 158px; height: 86px; background: var(--paper); }

  /* Spine */
  .spine-title, .spine-author {
    position: absolute; writing-mode: vertical-rl; font-family: "Libre Bodoni", serif; font-size: 25px; white-space: nowrap;
    z-index: 1;
  }
  .spine-title { left: 549px; top: 85px; color: #fff; }
  .spine-author { left: 549px; top: 514px; color: var(--spine-lime); }
  .spine-mark { position: absolute; left: 546px; top: 732px; width: 36px; text-align: center; z-index: 1;
    font-family: "Source Serif 4", serif; font-size: 5.5px; color: #111; letter-spacing: .05em; }
  .spine-mark .dot { width: 24px; height: 24px; margin: 0 auto 2px; border-radius: 50%; background: #111; }

  /* Front cover */
  .classroom-art { position: absolute; left: 721px; top: 171px; width: 347px; height: 165px; z-index: 1;
    background: radial-gradient(ellipse at 50% 60%, rgba(210,220,215,.55), rgba(160,180,170,.25) 60%, rgba(160,180,170,0) 100%); }
  .title-frame { position: absolute; left: 682px; top: 308px; width: 268px; height: 386px; border: 1.5px solid var(--edition-rule); border-radius: 26px; z-index: 1; }
  .title-card {
    position: absolute; left: 688px; top: 312px; width: 257px; height: 377px; border-radius: 22px; z-index: 1;
    background: linear-gradient(170deg, rgba(220,228,222,.92), rgba(236,250,210,.95) 60%, rgba(240,255,210,.97));
    text-align: center;
  }
  .title {
    margin-top: 30px; font-family: "Libre Bodoni", serif; font-weight: 400; font-size: 37px; line-height: 54px;
    color: var(--title-green); letter-spacing: -.01em;
  }
  .edition { position: relative; margin-top: 16px; font-family: "Libre Bodoni", serif; font-size: 19px; color: var(--title-green); }
  .edition::before, .edition::after { content: ""; position: absolute; top: 50%; width: 56px; height: 1.5px; background: var(--edition-rule); }
  .edition::before { left: 12px; } .edition::after { right: 12px; }
  .author { margin-top: 22px; font-family: "Libre Baskerville", serif; font-weight: 700; font-size: 20px; color: var(--title-green); }
  .subtitle { position: absolute; left: 636px; top: 714px; width: 420px; z-index: 1;
    font-family: "Libre Baskerville", serif; font-weight: 700; font-size: 13.5px; line-height: 18.5px; color: var(--subtitle-ink); }
</style>
</head>
<body>
<div class="canvas">
  <svg class="crop-marks" width="1200" height="1028" viewBox="0 0 1200 1028">
    <g stroke="var(--crop)" stroke-width="1">
      <line x1="65" y1="42" x2="65" y2="101"/><line x1="1135" y1="42" x2="1135" y2="101"/>
      <line x1="65" y1="924" x2="65" y2="984"/><line x1="1135" y1="924" x2="1135" y2="984"/>
      <line x1="12" y1="127" x2="35" y2="127"/><line x1="12" y1="899" x2="35" y2="899"/>
      <line x1="1167" y1="127" x2="1189" y2="127"/><line x1="1167" y1="899" x2="1189" y2="899"/>
    </g>
    <g stroke="var(--crop)" stroke-width="1" stroke-dasharray="3 2">
      <line x1="578" y1="45" x2="578" y2="101"/><line x1="621" y1="45" x2="621" y2="101"/>
      <line x1="578" y1="924" x2="578" y2="980"/><line x1="621" y1="924" x2="621" y2="980"/>
    </g>
  </svg>

  <div class="cover">
    <section class="back-panel">
      <div class="blurb">
        <p>Lorem ipsum dolor sit amet, consectetuer adipiscing elit, sed diam nonummy nibh euismod tincidunt ut laoreet dolore magna aliquam erat volutpat ut.</p>
        <p>Ut wisi enim ad minim veniam, quis nostrud exerci tation ullamcorper suscipit lobortis nisl ut aliquip ex ea commodo consequat. Duis autem vel eum iriure dolor in hendrerit in vulputate velit .</p>
        <p>Duis autem vel eum iriure dolor in hendrerit in vulputate velit . Duis autem vel eum iriure dolor in hendrerit in vulputate velit .</p>
      </div>
      <div class="column-rule"></div>
      <div class="author-photo" role="img" aria-label="Portrait photograph of the author"></div>
      <div class="about">
        <h2>About the Author</h2>
        <p>Amet, consectetuer adipiscing elit, sed diam nonummy nibh euismod tincidunt ut laoreet dolore magna aliquam erat volutpat ut.</p>
        <p>Ut wisi enim ad minim veniam, quis nostrud exerci tation ullamcorper suscipit lobortis nisl ut aliquip ex ea commodo consequat. Duis autem vel eum iriure dolor in hendrerit in vulputate velit .</p>
      </div>
      <div class="publisher-mark"><span class="dot"></span><span>HALVENMOOR PRESS</span></div>
      <div class="isbn-space"></div>
    </section>

    <div class="spine-title">The Lantern Keeper's Winter Ledger</div>
    <div class="spine-author">Malcolm Pettigrew</div>
    <div class="spine-mark"><div class="dot"></div>HALVENMOOR</div>

    <div class="classroom-art" role="img" aria-label="Illustration of empty school desks and chairs, one chair in orange and purple"></div>
    <div class="title-frame"></div>
    <div class="title-card">
      <h1 class="title">The Lantern<br>Keeper's<br>Winter<br>Ledger</h1>
      <div class="edition">2nd Edition</div>
      <div class="author">Malcolm Pettigrew</div>
    </div>
    <p class="subtitle">a neglected chapter of harbour trade, river tolls and market charter reform</p>
  </div>
</div>
</body>
</html>
```